Cybersecurity firm needs marketing template for professional services

Looking for a flyer design we can use as a template to market ten professional cybersecurity services (Pen Testing, V-CISO, SOC 2, VELMORA, etc). Each flyer will explain WHAT the service is, WHO needs it, DIFFERENT TYPES and SCOPE. Clean look/ lots of white space/ elevated graphics, Attached is a basic example but we are looking for something to WOW us.

```html
<!DOCTYPE html>
<html lang="en">
<head>
<meta charset="utf-8">
<title>Business Template Flyer</title>
<link rel="stylesheet" href="https://fonts.googleapis.com/css2?family=Oswald:wght@400;500&family=Open+Sans:wght@400&family=Questrial&display=swap">
<style>
  :root {
    --page-bg: #f3f4f6;
    --paper: #ffffff;
    --ink: #2e2e2e;
    --ink-soft: #3a3a3a;
    --brand-grey: #9a9a9a;
    --brand-blue: #1f8fd6;
    --wave-deep: #1a86cf;
    --wave-mid: #5fb6e6;
    --wave-light: #cbe7f7;
    --wash: #e4f2fb;
  }
  * { margin: 0; padding: 0; box-sizing: border-box; }
  html, body { width: 1200px; height: 1200px; overflow: hidden; }
  body { background: var(--page-bg); font-family: "Open Sans", sans-serif; color: var(--ink); position: relative; }

  .flyer {
    position: absolute; left: 214px; top: 70px; width: 766px; height: 1048px;
    background: linear-gradient(170deg, var(--paper) 0%, var(--paper) 45%, var(--wash) 100%);
    overflow: hidden;
  }

  .wave { position: absolute; }
  .wave--right {
    right: 0; top: 0; width: 170px; height: 720px;
    background: linear-gradient(200deg, rgba(95,182,230,0.15) 0%, rgba(26,134,207,0.55) 45%, rgba(95,182,230,0.35) 75%, rgba(203,231,247,0) 100%);
    border-radius: 120px 0 0 160px;
  }
  .wave--left {
    left: 0; top: 374px; width: 190px; height: 180px;
    background: linear-gradient(115deg, rgba(26,134,207,0.65) 0%, rgba(95,182,230,0.45) 55%, rgba(203,231,247,0) 100%);
    border-radius: 0 140px 90px 0;
  }
  .wave--base {
    right: 0; bottom: 0; width: 766px; height: 330px;
    background: linear-gradient(160deg, rgba(203,231,247,0) 20%, rgba(95,182,230,0.45) 100%);
  }

  .brand { position: absolute; left: 0; right: 0; top: 170px; text-align: center; }
  .brand__mark {
    width: 44px; height: 44px; border-radius: 50%; background: var(--brand-blue);
    margin: -70px auto 26px;
  }
  .brand__name { font-family: "Questrial", sans-serif; font-size: 40px; letter-spacing: -0.5px; color: var(--brand-grey); line-height: 1; }
  .brand__services { margin-top: 12px; font-family: "Questrial", sans-serif; font-size: 19px; color: #6f6f6f; letter-spacing: 0.5px; }
  .brand__services span { color: var(--brand-blue); padding: 0 4px; }

  .halo {
    position: absolute; left: 146px; top: 314px; width: 456px; height: 456px; border-radius: 50%;
    background: radial-gradient(circle at 50% 40%, rgba(255,255,255,0.95) 0%, rgba(245,248,250,0.9) 60%, rgba(225,232,238,0.8) 100%);
    box-shadow: 0 30px 40px -20px rgba(120,130,140,0.35), inset 0 0 0 2px rgba(255,255,255,0.9);
  }

  .headline { position: absolute; left: 0; right: 0; top: 410px; text-align: center; }
  .headline__kicker { font-family: "Oswald", sans-serif; font-weight: 400; font-size: 30px; letter-spacing: 12px; color: var(--ink); padding-left: 12px; }
  .headline__title { font-family: "Oswald", sans-serif; font-weight: 500; font-size: 76px; line-height: 1; letter-spacing: 1px; color: var(--ink); margin-top: 4px; }
  .headline__intro { margin-top: 22px; font-size: 15.5px; line-height: 22px; color: var(--ink-soft); }
  .headline__intro p + p { margin-top: 2px; }

  .points { position: absolute; left: 50px; top: 806px; width: 680px; display: grid; grid-template-columns: 354px 326px; row-gap: 26px; }
  .point { display: flex; align-items: center; gap: 12px; }
  .point__num {
    flex: 0 0 26px; width: 26px; height: 26px; border-radius: 50%; background: var(--ink);
    color: #fff; font-size: 15px; font-weight: 400; display: flex; align-items: center; justify-content: center;
  }
  .point__text { font-size: 10.8px; line-height: 13.5px; color: var(--ink); }
</style>
</head>
<body>
  <main class="flyer">
    <div class="wave wave--base" role="img" aria-label="Soft light blue wash rising toward the lower right"></div>
    <div class="wave wave--right" role="img" aria-label="Flowing translucent blue smoke ribbon along the right edge"></div>
    <div class="wave wave--left" role="img" aria-label="Flowing translucent blue smoke ribbon entering from the left"></div>

    <header class="brand">
      <div class="brand__mark"></div>
      <div class="brand__name">Northvale Group</div>
      <div class="brand__services">Cybersecurity<span>|</span>Risk<span>|</span>Audit<span>|</span>Advisory</div>
    </header>

    <div class="halo"></div>

    <section class="headline">
      <div class="headline__kicker">BUSINESS</div>
      <h1 class="headline__title">TEMPLATE</h1>
      <div class="headline__intro">
        <p>Lorem Ipsum is simply dummy text<br>of the printing and typesetting industry.</p>
        <p>Lorem Ipsum has been the industry's standard<br>scrambled it to make a type specimen book.</p>
      </div>
    </section>

    <section class="points">
      <div class="point">
        <div class="point__num">1</div>
        <div class="point__text">Lorem ipsum dolor sit amet, consectetur adipiscing elit.<br>Etiam iaculis dolor a ligula tincidunt, a aliquet nulla porta.<br>Quisque eget arcu metus.<br>Suspendisse potenti.</div>
      </div>
      <div class="point">
        <div class="point__num">2</div>
        <div class="point__text">Sed non libero sed mauris placerat venenatis.<br>Quisque mauris nunc, gravida ut nunc at, egestas<br>Suspendisse nec turpis sem.<br>Cras vehicula ut diam nec cursus.</div>
      </div>
      <div class="point">
        <div class="point__num">3</div>
        <div class="point__text">Mauris accumsan rhoncus justo, vitae sollicitudin<br>Vivamus a maximus nisl.<br>Nulla facilisi.<br>Morbi posuere leo lacus, at interdum enim viverra ut.<br>Nullam id mattis augue.</div>
      </div>
      <div class="point">
        <div class="point__num">4</div>
        <div class="point__text">Nulla rutrum maximus egestas.<br>Cum sociis natoque penatibus et magnis dis parturient<br>Vivamus facilisis sem sed magna semper, id aliquam.<br>Nullam faucibus arcu et arcu feugiat luctus</div>
      </div>
    </section>
  </main>
</body>
</html>
```